New Branding Business Card Design

Redesign business card according to new branding update.

** The design received so far are single color + BLACK.
I'd encourage designer to use different tones of blue / purple as described in the Designer Brief color palette

Target Market(s)

International

Industry/Entity Type

Medical Equipment

Contact Information for Business Card

Logo on one side (Designer can decide if they want to move certain info from the other side to save space)

Main body info (company name, individual name in both English and Chinese, contact info etc) on the other
Prefer a 'cleaner' layout - vs 'all over the place'
Prefer flush left alignment

Font styles to use
Sans Serif

Requirements
Must have
• Key info
• (Company name (English)): VORAM (HK) Limited
• (Name (English)): Marcus L. Pryde
• (Credential): FCPA, FHKSI
• (Title): Founder, Managing Director & CEO
• For the following info, designers decide whether to use colon or no colon, stroke separator, or use icon gfx for T (for telephone fixed line, M for mobile etc.)
• T: +852 3517 VORAM / +852 3517 4062
• M: +852 6243 7719 / + 86 139 2745 3186
• E: marcus.l.pryde@voram-example.hk
Nice to have
• Depending on the space and spacing available designers can add or use fuller title and other info
• Title: Chairman of the Executive Committee, Founder, Managing Director & CEO
• (Name (Chinese)): 林書恒
Should not have
• One of our business entities a long company name that cannot be broken into 2 lines
• makes vertical implementation almost impossible

```html
<!DOCTYPE html>
<html lang="en">
<head>
<meta charset="utf-8">
<title>VORAM (HK) Limited – Business Card</title>
<link href="https://fonts.googleapis.com/css2?family=Red+Hat+Display:wght@400;500;700;800&family=Noto+Sans+TC:wght@400&display=swap" rel="stylesheet">
<style>
  :root {
    --backdrop: #e9e6e1;
    --purple-deep: #4a2580;
    --purple-soft: #7b58ab;
    --white: #ffffff;
    --front-light: #ffffff;
    --front-shade: #e3e5ea;
    --blue-deep: #1f3fa8;
    --blue-mid: #1f5fc4;
    --blue-bright: #1b8ad8;
  }
  * { margin: 0; padding: 0; box-sizing: border-box; }
  html, body { width: 900px; height: 1200px; overflow: hidden; }
  body {
    background: var(--backdrop);
    font-family: "Red Hat Display", "Helvetica Neue", Arial, sans-serif;
    position: relative;
  }
  .card {
    position: absolute;
    left: 80px;
    width: 733px;
    height: 428px;
    border-radius: 22px;
    overflow: hidden;
  }
  .card-front { top: 128px; }
  .card-back { top: 646px; }
  .card-surface {
    position: absolute;
    inset: 0;
  }
  .card-front .card-surface {
    background: linear-gradient(125deg, var(--front-shade) 0%, var(--front-light) 35%, var(--front-shade) 60%, var(--front-light) 80%, var(--front-shade) 100%);
  }
  .card-back .card-surface {
    background: linear-gradient(120deg, var(--blue-mid) 0%, var(--blue-deep) 30%, var(--blue-bright) 55%, var(--blue-deep) 75%, var(--blue-bright) 100%);
  }
  .card-content { position: absolute; left: 68px; top: 80px; color: var(--purple-deep); }
  .company-name { font-size: 37px; font-weight: 700; letter-spacing: 0.2px; line-height: 1; }
  .person-name { margin-top: 18px; font-size: 24px; font-weight: 800; line-height: 1; }
  .person-name .name-zh {
    font-family: "Noto Sans TC", sans-serif;
    font-weight: 400;
    color: var(--purple-soft);
  }
  .person-name .sep { font-weight: 500; color: var(--purple-soft); }
  .credentials { margin-top: 7px; font-size: 16px; font-weight: 700; }
  .titles { margin-top: 20px; font-size: 17px; font-weight: 500; color: var(--purple-soft); line-height: 24px; }
  .contacts { margin-top: 18px; list-style: none; }
  .contact-row { display: flex; align-items: center; height: 30px; font-size: 17px; font-weight: 500; }
  .contact-tag {
    width: 20px; height: 20px; border-radius: 4px;
    background: var(--purple-deep); color: var(--white);
    font-size: 13px; font-weight: 700;
    display: flex; align-items: center; justify-content: center;
    margin-right: 9px;
  }
  .brand-lockup {
    position: absolute; left: 130px; top: 166px;
    display: flex; align-items: center;
  }
  .brand-square { width: 98px; height: 98px; border-radius: 8px; background: var(--white); margin-right: 20px; }
  .brand-name { color: var(--white); font-size: 38px; font-weight: 500; letter-spacing: 0.3px; }
</style>
</head>
<body>
  <section class="card card-front">
    <div class="card-surface" role="img" aria-label="Soft white and pale grey faceted background"></div>
    <div class="card-content">
      <h1 class="company-name">VORAM (HK) LIMITED</h1>
      <p class="person-name">MARCUS L. PRYDE <span class="sep">/</span> <span class="name-zh">林書恒</span></p>
      <p class="credentials">FCPA, FHKSI</p>
      <p class="titles">Chairman of the Executive Committee<br>Founder, Managing Director &amp; CEO</p>
      <ul class="contacts">
        <li class="contact-row"><span class="contact-tag">P</span>+852 3517 VORAM / +852 3517 4062</li>
        <li class="contact-row"><span class="contact-tag">M</span>+852 6243 7719 / + 86 139 2745 3186</li>
        <li class="contact-row"><span class="contact-tag">E</span>marcus.l.pryde@voram-example.hk</li>
      </ul>
    </div>
  </section>

  <section class="card card-back">
    <div class="card-surface" role="img" aria-label="Blue faceted background in deep and bright blue tones"></div>
    <div class="brand-lockup">
      <span class="brand-square"></span>
      <span class="brand-name">VORAM (HK) LIMITED</span>
    </div>
  </section>
</body>
</html>
```